need corporate, modern business card created for Consulting Company

I need a slick business card using elements from my website, as well as, integrating my pixelforge-created logo (see files).

The business card needs to be:
1. Corporate and modern
2. Clean and professional

I've included a PSD with the logo/icon that you can use to create it. Feel free to try a metallic finish on the logo, make it bigger/small, underlay it. Whatever you need to do to make my card stand out.

Try a black background, or white background or gray.

The idea is for my card to be memorable as well as professional and corporate.

Target Market(s)

Corporate business in the US and Canada.

Industry/Entity Type

Business

Contact Information for Business Card

Enterprise Advancing Solutions
Martin Coble, Senior Partner
office: 1 877 555 0143
mobile: 1 519 555 0172
website: http://www.velmorant.com

Requirements
Must have
• Card-related information
• corporate, yet modern
• clean and professional
• incorporate the icon only
• must have an editable form when complete!
Nice to have
• metallic icon might be cool
• try it with white or black

```html
<!DOCTYPE html>
<html lang="en">
<head>
<meta charset="utf-8">
<title>Velmorant Business Card</title>
<link rel="stylesheet" href="https://fonts.googleapis.com/css2?family=Open+Sans:wght@400;700&display=swap">
<style>
  :root {
    --stage: #d9dce0;
    --card-blue: #2f67b8;
    --card-black: #1f1f20;
    --crescent-grey: #a9aaad;
    --ink-white: #ffffff;
  }
  html, body {
    margin: 0;
    width: 1200px;
    height: 865px;
    overflow: hidden;
    background: var(--stage);
    font-family: "Open Sans", Arial, sans-serif;
  }
  .business-card {
    position: absolute;
    left: 100px;
    top: 147px;
    width: 1000px;
    height: 571px;
    background: var(--card-blue);
    overflow: hidden;
    box-shadow: 0 10px 30px rgba(0,0,0,0.18);
  }
  .card-shapes {
    position: absolute;
    inset: 0;
  }
  .shape-black { fill: var(--card-black); }
  .shape-crescent { fill: var(--crescent-grey); stroke: var(--card-black); stroke-width: 7; }
  .brand {
    position: absolute;
    left: 120px;
    top: 252px;
    display: flex;
    align-items: center;
    gap: 22px;
  }
  .brand-mark {
    width: 54px;
    height: 54px;
    background: var(--card-blue);
  }
  .brand-name {
    color: var(--ink-white);
    font-weight: 700;
    font-size: 66px;
    line-height: 1;
    letter-spacing: -1px;
  }
  .contact-block {
    position: absolute;
    right: 62px;
    top: 62px;
    text-align: right;
    color: var(--ink-white);
  }
  .person-name {
    font-weight: 700;
    font-size: 29px;
    line-height: 1.2;
    margin: 0;
  }
  .person-title {
    font-size: 27px;
    line-height: 1.2;
    margin: 0 0 70px;
  }
  .contact-line {
    font-size: 24px;
    line-height: 34px;
    margin: 0;
    display: flex;
    justify-content: flex-end;
    align-items: center;
    gap: 8px;
  }
  .contact-icon {
    width: 20px;
    height: 20px;
    fill: var(--ink-white);
  }
  .contact-gap { margin-top: 18px; }
</style>
</head>
<body>
  <div class="business-card">
    <svg class="card-shapes" viewBox="0 0 1000 571" width="1000" height="571">
      <path class="shape-crescent" d="M360,-5 L480,-5 C650,120 700,380 650,580 L550,580 C640,300 580,60 360,-5 Z"/>
      <path class="shape-black" d="M0,0 L360,0 C590,50 650,280 552,571 L0,571 Z"/>
    </svg>

    <div class="brand">
      <span class="brand-mark"></span>
      <span class="brand-name">velmorant</span>
    </div>

    <div class="contact-block">
      <p class="person-name">Dorian Welsh-Hale</p>
      <p class="person-title">Consultant</p>
      <p class="contact-line">047,12th floor,Plaza</p>
      <p class="contact-line">Harbour Road QTN</p>
      <p class="contact-line">012 345 6789
        <svg class="contact-icon" viewBox="0 0 24 24"><path d="M6.6 10.8a15 15 0 0 0 6.6 6.6l2.2-2.2a1 1 0 0 1 1-.25 11.4 11.4 0 0 0 3.6.6 1 1 0 0 1 1 1V20a1 1 0 0 1-1 1A17 17 0 0 1 3 4a1 1 0 0 1 1-1h3.5a1 1 0 0 1 1 1c0 1.25.2 2.45.6 3.6a1 1 0 0 1-.25 1z"/></svg>
      </p>
      <p class="contact-line">012 345 6789
        <svg class="contact-icon" viewBox="0 0 24 24"><path d="M6 2h9v5H6zM3 8h18v13H3zm3 3v2h4v-2zm0 4v2h4v-2zm7-4v2h5v-2zm0 4v2h5v-2z"/></svg>
      </p>
      <p class="contact-line">urname@email.com
        <svg class="contact-icon" viewBox="0 0 24 24"><path d="M2 5h20v14H2zm2 2v.5l8 5.5 8-5.5V7l-8 5.2z"/></svg>
      </p>
      <p class="contact-line contact-gap">urname@email.com</p>
      <p class="contact-line">www.yourwebsitename.com</p>
    </div>
  </div>
</body>
</html>
```